Premium Personal Brand — Facebook Banner (Used Across All Platforms)

Update — Additional Color Direction
In addition to the dark charcoal/slate direction already described, I'm also interested in seeing variants with:
Dark navy blue — Deep, authoritative, intelligence-community feel. Same textured/matte treatment, not flat or bright.
Warm charcoal with steel blue accent — Keep the dark base but introduce a subtle steel blue gradient, accent line, or tonal shift. Sophisticated, modern, adds dimension without adding color noise.
Both should maintain the same premium, restrained, architectural feel described in the original brief. No bright blues, no corporate PowerPoint energy — think midnight, think depth, think weight.
Everything else in the brief remains the same.
I am building a premium personal brand as an executive advisor to founders ($5M+ revenue).
This contest is Facebook-banner–focused, but the design must represent a visual system that will be reused across:
- LinkedIn
- YouTube
I- nstagram
- X (Twitter)
- Website hero sections and other brand touchpoints
Think of the Facebook banner as the primary expression of the brand — not a one-off graphic.
This project is about discovering a high-end visual style and brand feel, not decoration.
What to design
Please submit one cohesive visual system, shown primarily as:
- Facebook banner (primary focus)
The same design language should clearly translate to all platforms listed above.
Designers are responsible for using the current recommended dimensions for each platform.
Quick clarification on background direction:
Backgrounds should have depth and texture, not flat color fields. Avoid pure white, light grey, or solid black backgrounds. Think matte, architectural materials — stone, graphite, concrete, steel — not blank canvases. Subtle tonal variation is encouraged. Obvious gradients or decorative patterns are not.
Text to use
Primary Headline:
- Your Business Is Too Valuable To Be Run On Hope.
Subheadline:
- You didn’t build a business to become its prisoner.
Name:
Paul Whitaker
The headline should be the dominant visual element.
Logo note (important)
My personal logo is currently being finalized.
For this contest:
- Use a simple “PW” monogram placeholder
- Clean, bold, geometric sans-serif
- Do not design a logo
- The winning design must allow an easy logo swap later.
Headshot note (important)
- Please do not include a headshot in the banner design.
- Most platforms display a circular profile image separately.
- The banner should stand on its own using typography, layout, and tone only.
- Design the banner assuming the profile photo will sit nearby, not inside the banner.
Style direction
The design should feel:
- Premium
- Calm
- Confident
- Restrained
- High-trust
- Dark, neutral backgrounds are preferred.
- Fewer elements are better than more.
Think:
- Owner-level advisor
- Private equity / boardroom tone
- Industrial, Modern, Minimalist, Elite, Architectural, not decorative
What to avoid
Please do not submit designs that feel:
- Promotional, hype-driven, or salesy
- Like a coach, guru, or agency
- Bright, colorful, or gradient-heavy
- Busy or over-designed
- Based on stock photos
- No motivational speaker energy.
Reaction test
- If someone sees this banner on Facebook (or later on LinkedIn, YouTube, etc.), the reaction should be:
“That person is serious. I’d trust them with important decisions.”
Final note
- I am not looking for many variations.
- I am looking for one strong visual direction you believe in.
Simple beats clever.
- Restraint beats decoration.

```html
<!DOCTYPE html>
<html lang="en">
<head>
<meta charset="utf-8">
<title>Paul Whitaker — Facebook Banner</title>
<link rel="stylesheet" href="https://fonts.googleapis.com/css2?family=Montserrat:wght@400;600;700&family=Inter:wght@400&family=Allura&display=swap">
<style>
  :root {
    --canvas: #e6e6e6;
    --ink-white: #ffffff;
    --ink-soft: #f1f1f1;
    --graphite-deep: #0b0b0c;
    --graphite-mid: #2b2b2d;
    --steel-light: #a9a9ab;
    --ember: #8a3a0c;
    --signature-gold: #f0a80a;
  }
  * { margin: 0; padding: 0; box-sizing: border-box; }
  html, body {
    width: 1052px;
    height: 1200px;
    overflow: hidden;
    background: var(--canvas);
  }
  .stage {
    position: relative;
    width: 1052px;
    height: 1200px;
  }
  .banner {
    position: absolute;
    left: 36px;
    top: 392px;
    width: 980px;
    height: 415px;
    overflow: hidden;
    box-shadow: 0 10px 24px rgba(0,0,0,0.35);
  }
  .banner-texture {
    position: absolute;
    inset: 0;
    background:
      radial-gradient(ellipse 45% 60% at 58% 85%, rgba(190,190,192,0.75), rgba(120,120,122,0.35) 45%, transparent 75%),
      radial-gradient(ellipse 30% 30% at 100% 100%, rgba(138,58,12,0.45), transparent 70%),
      radial-gradient(ellipse 30% 30% at 0% 100%, rgba(138,58,12,0.35), transparent 70%),
      radial-gradient(ellipse 60% 70% at 62% 35%, rgba(60,60,62,0.9), transparent 80%),
      linear-gradient(180deg, var(--graphite-deep) 0%, var(--graphite-mid) 55%, #3a2a20 100%);
  }
  .brand-name {
    position: absolute;
    left: 115px;
    top: 42px;
    font-family: "Montserrat", sans-serif;
    font-weight: 600;
    font-size: 19px;
    line-height: 19px;
    color: var(--ink-white);
  }
  .headline {
    position: absolute;
    left: 0;
    right: 0;
    top: 52px;
    text-align: center;
    font-family: "Montserrat", sans-serif;
    font-weight: 400;
    font-size: 50px;
    line-height: 60px;
    color: var(--ink-white);
    letter-spacing: 0.2px;
  }
  .headline strong { font-weight: 700; }
  .divider {
    position: absolute;
    left: 240px;
    top: 252px;
    width: 500px;
    height: 2px;
    background: var(--ink-soft);
  }
  .subheadline {
    position: absolute;
    left: 0;
    right: 0;
    top: 260px;
    text-align: center;
    font-family: "Inter", sans-serif;
    font-size: 19px;
    color: var(--ink-soft);
  }
  .signature {
    position: absolute;
    left: 0;
    right: 0;
    top: 292px;
    text-align: center;
    font-family: "Allura", cursive;
    font-size: 56px;
    line-height: 60px;
    color: var(--signature-gold);
  }
</style>
</head>
<body>
  <main class="stage">
    <section class="banner">
      <div class="banner-texture" role="img" aria-label="Dark brushed steel and perforated metal texture with faint orange ember sparks"></div>
      <div class="brand-name">Paul<br>Whitaker</div>
      <h1 class="headline">Your <strong>Business</strong> Is Too<br><strong>Valuable</strong> To Be Run<br>On <strong>Hope</strong>.</h1>
      <div class="divider"></div>
      <p class="subheadline">You didn’t build a business to become its prisoner.</p>
      <p class="signature">Paul Whitaker</p>
    </section>
  </main>
</body>
</html>
```